Ferrando Quispe Law Firm for Small and Medium Business: Website

We need a web design that includes coding for the Wix platform, for a new company based in Santiago, Chile, called Ferrando Quispe, Abogados y Consultores. The company is essentially a law firm, with additional advisory services in accounting, tax management and finance. The main target of the company are founders, CEOs or C-level executives of small or medium companies based in Chile.
The main menu of the web page must have the following tab options:
- Home - About us - Services – How we work -Blog – FAQ -Contact
Our main services are:

1.- Commercial and corporate law advisory
2.- Legal defense in civil, criminal, labor and family matters (litigation and arbitration)
3.- Bankruptcy and reorganization of companies
4.- Collection and recovery of assets
5.- Asset protection
6.- Financial and tax advice

We want to highlight the following services:

-Bankruptcy and reorganization of companies
-Judicial defense in civil matters
-Financial and tax advice

In addition to these services, the following will be offered:
-Lawyer at your home for special cases
-Half hour free consultation
-Monthly service packages

The final design should communicate confidence, business savvy and high execution standards and quality.

Target Market(s)

The main target of the company are founders, CEOs or C-level executives of small or medium companies based in Chile.

Industry/Entity Type

Legal industry

Coding

Coded - Design and coding required

Number of Pages Required

5+ page

Font styles to use
Serif

Requirements
Must have
• 1. Big banners para destacar los siguientes servicios: -Bankruptcy and reorganization of companies -Judicial defense in civil matters -Financial and tax advice 2. Call to action para agendar consulta legal. 3. Destacar los siguientes servicios: -Lawyer at your home for special cases -Half hour free consultation -Monthly service packages 3. Página para explicar cómo se cobra (precios transparentes): ver el siguiente sitio web: https://www.brindlemoorlegal.example/how 4. Links to Facebook, Instagram and Linkedin 5. Connection to Whatsapp.
Should not have
• Look old fashioned

```html
<!DOCTYPE html>
<html lang="en">
<head>
<meta charset="utf-8">
<title>Ferrando Quispe, Abogados y Consultores</title>
<link href="https://fonts.googleapis.com/css2?family=Poppins:wght@400;500;600;700&family=Questrial&display=swap" rel="stylesheet">
<style>
:root{
  --black:#000;
  --ink:#0c0c0c;
  --text:#333;
  --muted:#555;
  --gold:#c9a83a;
  --gold-dark:#9c7d1a;
  --gold-grad:linear-gradient(180deg,#e6cd62 0%,#c7a533 55%,#a8871c 100%);
  --light:#f4f4f4;
  --line:#e3e3e3;
  --white:#fff;
}
*{box-sizing:border-box;margin:0;padding:0}
html,body{width:1200px;height:4580px;overflow:hidden}
body{font-family:"Poppins",sans-serif;color:var(--text);background:var(--white);position:relative}
.abs{position:absolute}
section,header,footer{position:relative;width:1200px}
h2.section-title{font-family:"Questrial",sans-serif;font-weight:400;font-size:36px;color:#222;text-align:center;position:absolute;left:0;width:100%}
.title-rule{position:absolute;left:568px;width:64px;height:2px;background:var(--gold)}
.btn{position:absolute;background:var(--gold-grad);color:#111;font-weight:600;font-size:14px;display:flex;align-items:center;justify-content:center;border-radius:3px;box-shadow:0 2px 0 #7d6412}
.brand{display:flex;align-items:center;gap:12px}
.brand-mark{width:52px;height:52px;background:var(--gold)}
.brand-name{font-family:"Poppins",sans-serif;font-weight:400;font-size:34px;color:var(--gold);letter-spacing:.5px}

/* header */
.site-header{height:107px;background:var(--black)}
.site-header .brand{position:absolute;left:112px;top:24px}
.social-top{position:absolute;left:800px;top:10px;display:flex;gap:9px}
.social-top span,.footer-social span{width:26px;height:26px;border:1.5px solid #ccc;border-radius:4px;display:block}
.phone-pill{position:absolute;left:950px;top:8px;width:138px;height:30px;background:var(--gold-grad);border-radius:3px;font-size:14px;color:#111;font-weight:500;display:flex;align-items:center;justify-content:center;gap:6px}
.main-nav{position:absolute;left:563px;top:56px;display:flex;gap:26px;font-size:13px;color:#fff}
.main-nav a{color:#fff;text-decoration:none}
.main-nav a.active{border-bottom:1px solid #fff}

/* hero */
.hero{height:512px;background:var(--ink)}
.hero h1{position:absolute;left:113px;top:100px;width:520px;font-weight:600;font-size:36px;line-height:52px;color:#fff}
.hero p{position:absolute;left:113px;top:262px;width:490px;font-size:16px;line-height:29px;color:#fff}
.hero-art{position:absolute;left:684px;top:17px;width:436px;height:463px;border-radius:8px;background:radial-gradient(ellipse at 50% 60%,#2d3a6b 0%,#1c2b4d 35%,#122 65%,var(--ink) 85%)}

/* services */
.services{height:519px}
.svc-card{position:absolute;top:170px;width:292px;text-align:center}
.svc-card svg{display:block;margin:0 auto 20px}
.svc-card h3{font-family:"Questrial",sans-serif;font-weight:400;font-size:17px;line-height:25px;color:#222;margin-bottom:10px}
.svc-card p{font-size:13px;line-height:22px;color:var(--muted);padding:0 20px}
.svc-card .more{display:inline-block;margin-top:12px;font-size:13px;color:#444;border-bottom:1px solid #bbb;padding-bottom:2px}
.vsep{position:absolute;top:165px;width:1px;height:290px;background:var(--line)}
.arrow-btn{position:absolute;width:32px;height:32px;border:1px solid #ddd;background:#fff;display:flex;align-items:center;justify-content:center;font-size:16px;color:#333}
.hr-rule{position:absolute;left:160px;top:518px;width:880px;height:1px;background:var(--line)}

/* about */
.about{height:598px}
.about .tagline{position:absolute;left:0;width:100%;top:149px;text-align:center;font-size:9px;letter-spacing:3px;color:var(--gold-dark)}
.about-art{position:absolute;left:162px;top:190px;width:393px;height:300px;background:linear-gradient(135deg,#f8d9c6,#f1c2a8 60%,#e8ad92)}
.about-badge{position:absolute;left:463px;top:424px;width:112px;height:112px;background:var(--gold-grad);border:4px solid #fff;box-shadow:0 2px 8px rgba(0,0,0,.2)}
.about h3{position:absolute;left:620px;top:222px;width:420px;font-size:16px;font-weight:600;line-height:27px;color:#222}
.about p{position:absolute;left:620px;top:285px;width:420px;font-size:13px;line-height:23px;color:var(--muted)}

/* extras */
.extras{height:660px;background:var(--black)}
.extras .kicker{position:absolute;left:0;width:100%;top:92px;text-align:center;font-size:15px;color:#ddd}
.extras h2.section-title{color:#fff}
.extras-frame{position:absolute;left:162px;top:218px;width:878px;height:265px;border:1px solid #444;border-radius:4px}
.extra-card{position:absolute;text-align:center;color:#fff}
.extra-card svg{display:block;margin:0 auto 16px}
.extra-card h3{font-weight:500;font-size:16px;line-height:25px;margin-bottom:12px}
.extra-card p{font-size:13px;line-height:22px;color:#e9e9e9}
.extra-card.featured{background:var(--gold-grad);border-radius:4px;box-shadow:0 0 24px rgba(0,0,0,.6)}
.extra-card.featured h3{color:#1a1a1a}
.extra-card.featured p{color:#3a2f0a}

/* how we work */
.how{height:608px;background:linear-gradient(180deg,#fafafa,#f5f5f5)}
.step{position:absolute;width:260px}
.step svg{position:absolute;left:0;top:0}
.step h3{margin-left:79px;font-size:13.5px;font-weight:500;line-height:22px;color:#222}
.step p{margin-left:79px;margin-top:7px;font-size:13px;line-height:22px;color:var(--muted)}
.track{position:absolute;left:162px;width:900px;height:1px;background:#ddd}
.dot{position:absolute;width:9px;height:9px;border:1.5px solid #777;border-radius:50%;background:#fff}

/* blog */
.blog{height:679px}
.post{position:absolute;top:179px;width:279px}
.post-img{height:212px;position:relative}
.post-date{position:absolute;left:0;top:0;width:59px;height:60px;background:var(--gold-grad);text-align:center;color:#111;font-size:21px;line-height:26px;padding-top:4px}
.post-date small{display:block;font-size:12px;line-height:14px}
.post h3{margin-top:20px;padding-left:16px;border-left:2px solid var(--gold);font-size:13px;font-weight:600;line-height:22px;color:#222}
.post p{padding-left:18px;margin-top:6px;font-size:13px;line-height:22px;color:var(--muted)}
.post .more{margin-left:18px;margin-top:9px;display:inline-block;font-size:13px;color:#444;border-bottom:1px solid #bbb}

/* contact */
.contact{height:533px;background:var(--light)}
.field{position:absolute;height:45px;background:#fff;border:1px solid #e5e5e5;display:flex;align-items:center;font-size:12px;color:#888}
.field .ico{width:52px;display:flex;justify-content:center}
.field .ico svg{stroke:#aaa}
.field.area{align-items:flex-start;padding-top:14px}

/* footer */
.site-footer{height:363px;background:var(--black);color:#fff}
.site-footer h4{position:absolute;font-size:17px;font-weight:600;color:#fff}
.quick-links{position:absolute;left:162px;top:90px;list-style:none;font-size:13px;line-height:29px}
.quick-links li::before{content:"›";margin-right:14px;color:#ccc}
.contact-item{position:absolute;left:397px;display:flex;gap:13px}
.contact-item .badge{width:30px;height:30px;background:var(--gold-grad);border-radius:3px;display:flex;align-items:center;justify-content:center}
.contact-item b{font-weight:600;font-size:14px;display:block}
.contact-item span{font-size:13px;line-height:22px}
.site-footer .brand{position:absolute;left:758px;top:48px}
.site-footer .brand-mark{width:46px;height:46px}
.site-footer .brand-name{font-size:30px}
.footer-social{position:absolute;left:811px;top:136px;display:flex;gap:18px}
.footer-social span{width:30px;height:30px;border:none;background:var(--gold-grad)}
.copyright{position:absolute;left:758px;width:330px;top:196px;text-align:center;font-size:13px;line-height:22px}
</style>
</head>
<body>

<header class="site-header">
  <div class="brand"><span class="brand-mark"></span><span class="brand-name">Ferrando Quispe</span></div>
  <div class="social-top" aria-label="Social links"><span></span><span></span><span></span><span></span></div>
  <div class="phone-pill">
    <svg width="12" height="12" viewBox="0 0 24 24"><path d="M6 2l4 4-2 3c1 3 4 6 7 7l3-2 4 4-3 4C10 22 2 14 2 5z" fill="#111"/></svg>123 456 7890
  </div>
  <nav class="main-nav">
    <a class="active">Home</a><a>About Us</a><a>Services</a><a>How We Work</a><a>Blog</a><a>FAQs</a><a>Contact Us</a>
  </nav>
</header>

<section class="hero">
  <h1>We Deal With Bankruptcy And Reorganization of Companies</h1>
  <p>Lorem Ullamcorper suscipit lobortis nisl ut aliquip ex ea commodo conseq veleum riure dolor.</p>
  <div class="btn" style="left:113px;top:334px;width:248px;height:36px">Schedule Legal Consultation</div>
  <div class="hero-art" role="img" aria-label="Illustration of a lawyer at a desk on a large law book with scales of justice, pen, lightbulb and handcuffs"></div>
</section>

<section class="services">
  <h2 class="section-title" style="top:88px">Our Services</h2>
  <div class="title-rule" style="top:138px"></div>
  <div class="arrow-btn" style="left:98px;top:285px">‹</div>
  <div class="arrow-btn" style="left:1060px;top:285px">›</div>
  <div class="vsep" style="left:454px"></div>
  <div class="vsep" style="left:747px"></div>

  <div class="svc-card" style="left:152px">
    <svg width="80" height="62" viewBox="0 0 80 62" fill="none" stroke="#333" stroke-width="2"><rect x="6" y="8" width="26" height="44"/><rect x="40" y="16" width="34" height="36"/><path d="M12 18h14M12 26h14M12 34h14M46 24h6M58 24h6M46 32h6M58 32h6M46 40h6M58 40h6M2 52h76"/></svg>
    <h3>Bankruptcy &amp; Reorganization<br>of Companies</h3>
    <p>Lorem ipsum dolor sit ameteoer consectetuer adipiscing elit seddia nonummy nibh euismod</p>
    <span class="more">Read More</span>
  </div>
  <div class="svc-card" style="left:454px">
    <svg width="80" height="62" viewBox="0 0 80 62" fill="none" stroke="#333" stroke-width="2"><path d="M40 4v18M22 12h36M22 12l-6 12h12zM58 12l-6 12h12z"/><circle cx="40" cy="36" r="6"/><circle cx="24" cy="40" r="5"/><circle cx="56" cy="40" r="5"/><path d="M28 58c0-8 6-12 12-12s12 4 12 12M14 58c0-7 4-10 10-10M66 58c0-7-4-10-10-10"/></svg>
    <h3>Judicial Defense in<br>Civil Matters</h3>
    <p>Lorem ipsum dolor sit ameteoer consectetuer adipiscing elit seddia nonummy nibh euismod</p>
    <span class="more">Read More</span>
  </div>
  <div class="svc-card" style="left:754px">
    <svg width="80" height="62" viewBox="0 0 80 62" fill="none" stroke="#333" stroke-width="2"><rect x="18" y="6" width="44" height="18" rx="2"/><path d="M24 15h32M12 34h56v20H12zM20 42h40M28 54v6M52 54v6"/></svg>
    <h3>Financial &amp;<br>Tax Advice</h3>
    <p>Lorem ipsum dolor sit ameteoer consectetuer adipiscing elit seddia nonummy nibh euismod</p>
    <span class="more">Read More</span>
  </div>
  <div class="hr-rule"></div>
</section>

<section class="about">
  <h2 class="section-title" style="top:107px;color:#222">About <span style="color:var(--gold)">Ferrando Quispe</span></h2>
  <div class="tagline">ABOGADOS Y CONSULTORES</div>
  <div class="about-art" role="img" aria-label="Illustration of a person on a video call at a laptop beside law books and a plant"></div>
  <div class="about-badge"></div>
  <h3>Lorem ipsum dolor sit ametrtrt consectetuer tiscing elit sed diam nonummy nibh euis.</h3>
  <p>Sed diam nonummy nibh euismod tincidunt ut laoreet dolore magna aliquam erat volutpat. Ut wisi enim ad minim veniam, quis nostrud exerci tation ullamcorper suscipit lobortis nisl ut aliquip ex ea commodo consequat. Duis autem vel eum riure dolor in hendrerit in vulputate velit esse molestie consequat, vel illum dolore eu feugiat nulla faci Duis autem vel eum riure dolor in hendrerit in vulputate velit esse molestie</p>
  <div class="btn" style="left:617px;top:445px;width:110px;height:34px">Read More</div>
</section>

<section class="extras">
  <div class="kicker">In Addition To The Above Services</div>
  <h2 class="section-title" style="top:120px;color:#fff">Following Will Be Offered</h2>
  <div class="title-rule" style="top:178px"></div>
  <div class="extras-frame"></div>

  <div class="extra-card" style="left:172px;top:238px;width:265px">
    <svg width="66" height="62" viewBox="0 0 66 62" fill="none" stroke="#fff" stroke-width="2"><path d="M4 22L33 4l29 18M10 22v36h46V22"/><circle cx="22" cy="32" r="4"/><circle cx="33" cy="30" r="4"/><circle cx="44" cy="32" r="4"/><path d="M16 50c0-7 3-10 6-10M50 50c0-7-3-10-6-10M26 50c0-8 3-12 7-12s7 4 7 12"/></svg>
    <h3>Lawyer At Your Home For<br>Special Cases</h3>
    <p>Lorem ipsum dolor sit ameteoer consectetuer adipiscing elit seddia nonummy nibh euismod... (+)</p>
  </div>
  <div class="extra-card featured" style="left:448px;top:204px;width:304px;height:292px;padding-top:30px">
    <svg width="74" height="66" viewBox="0 0 74 66" fill="none" stroke="#1a1a1a" stroke-width="2"><rect x="28" y="2" width="20" height="12" rx="2"/><circle cx="37" cy="26" r="6"/><path d="M24 48c0-9 6-14 13-14s13 5 13 14M6 48h62M12 48v16M62 48v16"/><circle cx="12" cy="32" r="4"/><circle cx="62" cy="32" r="4"/></svg>
    <h3 style="margin-top:4px">Half Hour Free<br>Consultation</h3>
    <p>Lorem ipsum dolor sit ameteoer consectetuer adipiscing elit seddia nonummy nibh euismod... (+)</p>
  </div>
  <div class="extra-card" style="left:762px;top:238px;width:268px">
    <svg width="66" height="62" viewBox="0 0 66 62" fill="none" stroke="#fff" stroke-width="2"><rect x="6" y="8" width="54" height="50" rx="3"/><path d="M6 20h54M16 4v8M26 4v8M40 4v8M50 4v8"/><circle cx="33" cy="40" r="11"/><path d="M33 33v14"/></svg>
    <h3>Monthly Service<br>Packages</h3>
    <p>Lorem ipsum dolor sit ameteoer consectetuer adipiscing elit seddia nonummy nibh euismod... (+)</p>
  </div>
  <div class="btn" style="left:521px;top:528px;width:158px;height:34px">Contact Us Today</div>
</section>

<section class="how">
  <h2 class="section-title" style="top:86px">How We Work</h2>
  <div class="title-rule" style="top:138px"></div>

  <div class="track" style="top:177px"></div>
  <div class="dot" style="left:162px;top:173px"></div>
  <div class="dot" style="left:481px;top:173px"></div>
  <div class="dot" style="left:777px;top:173px"></div>
  <div class="track" style="top:373px"></div>
  <div class="dot" style="left:162px;top:369px"></div>
  <div class="dot" style="left:481px;top:369px"></div>
  <div class="dot" style="left:777px;top:369px"></div>

  <div class="step" style="left:160px;top:205px">
    <svg width="62" height="58" viewBox="0 0 62 58" fill="none" stroke="#333" stroke-width="2"><path d="M31 4v48M10 12h42M10 12l-7 16h14zM52 12l-7 16h14zM20 52h22"/></svg>
    <h3>Commercial &amp; Corporate<br>Law Advisory</h3>
    <p>Lorem ipsum dolor sit met consectetuer adipiscin elit nonummy nibheui... (+)</p>
  </div>
  <div class="step" style="left:460px;top:205px">
    <svg width="62" height="58" viewBox="0 0 62 58" fill="none" stroke="#333" stroke-width="2"><rect x="4" y="2" width="36" height="52"/><path d="M12 14h20M12 22h20M12 30h14"/><circle cx="44" cy="40" r="10"/></svg>
    <h3>Legal Defense In Civil,<br>Criminal, Labor &amp; Family<br>Matters</h3>
    <p>Lorem ipsum dolor sit met consectetuer adipiscin elit nonummy nibheui... (+)</p>
  </div>
  <div class="step" style="left:756px;top:205px">
    <svg width="62" height="58" viewBox="0 0 62 58" fill="none" stroke="#333" stroke-width="2"><path d="M4 26L31 4l27 22M10 22v32h42V22"/><rect x="22" y="32" width="18" height="22"/></svg>
    <h3>Bankruptcy &amp; Reorganization<br>of Companies</h3>
    <p>Lorem ipsum dolor sit met consectetuer adipiscin elit nonummy nibheui... (+)</p>
  </div>
  <div class="step" style="left:160px;top:403px">
    <svg width="62" height="58" viewBox="0 0 62 58" fill="none" stroke="#333" stroke-width="2"><circle cx="28" cy="28" r="22"/><circle cx="28" cy="28" r="12"/><path d="M28 20v16"/></svg>
    <h3>Collection And Recovery<br>of Assets</h3>
    <p>Lorem ipsum dolor sit met consectetuer adipiscin elit nonummy nibheui... (+)</p>
  </div>
  <div class="step" style="left:460px;top:403px">
    <svg width="62" height="58" viewBox="0 0 62 58" fill="none" stroke="#333" stroke-width="2"><path d="M4 30L22 14l18 16M10 26v20h24V26M4 52h30l14-10"/><circle cx="46" cy="14" r="8"/></svg>
    <h3>Asset<br>Protection</h3>
    <p>Lorem ipsum dolor sit met consectetuer adipiscin elit nonummy nibheui... (+)</p>
  </div>
  <div class="step" style="left:756px;top:403px">
    <svg width="62" height="58" viewBox="0 0 62 58" fill="none" stroke="#333" stroke-width="2"><rect x="26" y="4" width="30" height="24" rx="2"/><path d="M32 12h18M32 20h12"/><circle cx="16" cy="22" r="7"/><path d="M4 54c0-12 5-18 12-18s12 6 12 18"/></svg>
    <h3>Financial And<br>Tax Advice</h3>
    <p>Lorem ipsum dolor sit met consectetuer adipiscin elit nonummy nibheui... (+)</p>
  </div>
</section>

<section class="blog">
  <h2 class="section-title" style="top:95px">Latest Blog Posts</h2>
  <div class="title-rule" style="top:147px"></div>
  <div class="arrow-btn" style="left:103px;top:364px;width:30px;height:30px">‹</div>
  <div class="arrow-btn" style="left:1065px;top:364px;width:30px;height:30px">›</div>

  <article class="post" style="left:162px">
    <div class="post-img" role="img" aria-label="Illustration of a laptop, law books, gavel and glasses on a desk" style="background:linear-gradient(135deg,#fbe3d3,#f3c9b0)"><div class="post-date">10<small>August</small></div></div>
    <h3>Lorem ipsum dolor sit meteropere consectetuer adipiscin</h3>
    <p>Sed diam nonummy nibh euis moeder tincidunt utlaoreet dolore</p>
    <span class="more">Read More</span>
  </article>
  <article class="post" style="left:461px">
    <div class="post-img" role="img" aria-label="Illustration of law books, gavel and notes on a desk" style="background:linear-gradient(135deg,#fde8da,#f6d0b8)"><div class="post-date">11<small>August</small></div></div>
    <h3>Lorem ipsum dolor sit meteropere consectetuer adipiscin</h3>
    <p>Sed diam nonummy nibh euis moeder tincidunt utlaoreet dolore</p>
    <span class="more">Read More</span>
  </article>
  <article class="post" style="left:761px">
    <div class="post-img" role="img" aria-label="Illustration of a lawyer with a large document, books and gavel" style="background:linear-gradient(135deg,#fce6d8,#f4cdb4)"><div class="post-date">12<small>August</small></div></div>
    <h3>Lorem ipsum dolor sit meteropere consectetuer adipiscin</h3>
    <p>Sed diam nonummy nibh euis moeder tincidunt utlaoreet dolore</p>
    <span class="more">Read More</span>
  </article>
  <div class="btn" style="left:550px;top:590px;width:98px;height:32px">View All</div>
</section>

<section class="contact">
  <h2 class="section-title" style="top:62px">Contact Us</h2>
  <div class="title-rule" style="top:114px"></div>
  <div class="field" style="left:244px;top:169px;width:345px"><span class="ico"><svg width="14" height="14" viewBox="0 0 24 24" fill="none" stroke-width="2"><circle cx="12" cy="8" r="4"/><path d="M4 22c0-6 4-8 8-8s8 2 8 8"/></svg></span>Your Name*</div>
  <div class="field" style="left:610px;top:169px;width:345px"><span class="ico"><svg width="14" height="14" viewBox="0 0 24 24" fill="none" stroke-width="2"><path d="M12 22s7-7 7-13a7 7 0 0 0-14 0c0 6 7 13 7 13z"/><circle cx="12" cy="9" r="2.5"/></svg></span>Email*</div>
  <div class="field" style="left:244px;top:226px;width:345px"><span class="ico"><svg width="14" height="14" viewBox="0 0 24 24" fill="none" stroke-width="2"><path d="M6 2l4 4-2 3c1 3 4 6 7 7l3-2 4 4-3 4C10 22 2 14 2 5z"/></svg></span>Phone*</div>
  <div class="field" style="left:610px;top:226px;width:345px"><span class="ico"><svg width="14" height="14" viewBox="0 0 24 24" fill="none" stroke-width="2"><path d="M4 20h16M6 16l10-10 3 3-10 10H6z"/></svg></span>Inquiry For*</div>
  <div class="field area" style="left:244px;top:286px;width:711px;height:109px"><span class="ico"><svg width="14" height="14" viewBox="0 0 24 24" fill="none" stroke-width="2"><circle cx="12" cy="12" r="10"/><path d="M9 9a3 3 0 1 1 4 3v2M12 17v1"/></svg></span>How can we help you?</div>
  <div class="btn" style="left:525px;top:433px;width:150px;height:37px">Submit</div>
</section>

<footer class="site-footer">
  <h4 style="left:162px;top:47px">Quick Links</h4>
  <ul class="quick-links">
    <li>Home</li><li>About Us</li><li>Services</li><li>How We Work</li><li>Blog</li><li>FAQs</li><li>Contact Us</li>
  </ul>

  <h4 style="left:397px;top:47px">Contact Details</h4>
  <div class="contact-item" style="top:97px">
    <span class="badge"><svg width="14" height="14" viewBox="0 0 24 24"><path d="M12 22s7-7 7-13a7 7 0 0 0-14 0c0 6 7 13 7 13z" fill="#111"/></svg></span>
    <div><b>Address</b><span>12 Lorem Imsum, Street Name,<br>City Name, Country - 12345</span></div>
  </div>
  <div class="contact-item" style="top:180px">
    <span class="badge"><svg width="14" height="14" viewBox="0 0 24 24"><path d="M6 2l4 4-2 3c1 3 4 6 7 7l3-2 4 4-3 4C10 22 2 14 2 5z" fill="#111"/></svg></span>
    <div><b>Phone</b><span>123 456 7890</span></div>
  </div>
  <div class="contact-item" style="top:246px">
    <span class="badge"><svg width="14" height="14" viewBox="0 0 24 24"><rect x="2" y="5" width="20" height="14" fill="#111"/><path d="M2 5l10 8 10-8" stroke="#c9a83a" stroke-width="1.5" fill="none"/></svg></span>
    <div><b>Email</b><span>inquiry@ferrandoquispe.example</span></div>
  </div>

  <div class="brand"><span class="brand-mark"></span><span class="brand-name">Ferrando Quispe</span></div>
  <div class="footer-social" aria-label="Social links"><span></span><span></span><span></span><span></span></div>
  <div class="copyright">Copyright © 2021 Ferrando Quispe.<br>All Rights Reserved.</div>
</footer>

</body>
</html>
```